Newspaper Ad for Front page strip

Tavrenwick Lending is a micro lender operating in the Caribbean. This ad is for our Trinidad and Tobago location.
Would like to design a catchy banner ad for the front page of a daily newspaper. The ad should capture 1) that we offer unsecured loans up to $40,000. 2) customer can apply online or over the phone 3) that the process is quick.
We have included the a snapshot of our Instagram posts as well as the newspaper location and size of the ad.
We have booked this ad spot for the year so the more engaging we can make it the better. Maybe we can do a series of ads or weekly storyline . Let’s be creative.
https://www.instagram.com/tavrenwicklending/
www.tavrenwick lending.example
Target Market(s)
Mass population.
Industry/Entity Type
Banking
Look and feel

```html
<!DOCTYPE html>
<html lang="en">
<head>
<meta charset="utf-8">
<title>Tavrenwick Lending – Front Page Strip Series</title>
<link rel="stylesheet" href="https://fonts.googleapis.com/css2?family=Caveat:wght@600&family=Dancing+Script:wght@600&family=Montserrat:wght@400;700&family=Oswald:wght@600&display=swap">
<style>
  :root {
    --stage: #a6a7ab;
    --paper: #ffffff;
    --mint: #e4f1e8;
    --brand-green: #00934a;
    --deep-green: #0a6b37;
    --brand-red: #e2231a;
    --ink: #3a3a3a;
  }
  * { box-sizing: border-box; margin: 0; padding: 0; }
  html, body { width: 1200px; height: 1200px; overflow: hidden; }
  body { background: var(--stage); position: relative; font-family: "Montserrat", sans-serif; }

  .strip {
    position: absolute;
    top: 56px;
    width: 241px;
    height: 1087px;
    overflow: hidden;
    background: linear-gradient(180deg, var(--paper) 0%, var(--paper) 18%, var(--mint) 34%, var(--mint) 60%, var(--paper) 72%);
  }
  .strip--one { left: 165px; }
  .strip--two { left: 479px; }
  .strip--three { left: 791px; }

  .brand-name {
    position: absolute; top: 34px; left: 0; right: 0;
    text-align: center;
    font: 700 17px/1 "Montserrat", sans-serif;
    color: var(--brand-red);
  }
  .offer-intro {
    position: absolute; top: 103px; left: 0; right: 0;
    text-align: center;
    font: 600 46px/1 "Caveat", cursive;
    color: var(--ink);
  }
  .loan-type {
    position: absolute; top: 158px; left: 0; right: 0;
    text-align: center;
    font: 400 22px/26px "Montserrat", sans-serif;
    color: var(--brand-red);
  }
  .loan-amount {
    position: absolute; top: 230px; left: 0; right: 0;
    text-align: center;
    font: 600 60px/1 "Oswald", sans-serif;
    color: var(--brand-green);
    letter-spacing: -1px;
  }
  .photo-area {
    position: absolute; top: 324px; left: 0; width: 241px; height: 390px;
    background:
      linear-gradient(180deg, rgba(228,241,232,0) 0%, rgba(228,241,232,0) 80%, rgba(255,255,255,0.9) 100%),
      linear-gradient(160deg, #d9e9df 0%, #6b4a3a 30%, #2c2f3b 55%, #c9c3bb 75%, #e9ece9 100%);
  }
  .pin-graphic { position: absolute; left: 0; top: 0; width: 241px; height: 1087px; }
  .apply-note {
    position: absolute; top: 745px; left: 46px; width: 149px;
    text-align: center;
    font: 400 15px/22.7px "Montserrat", sans-serif;
    color: var(--paper);
  }
  .speed-line {
    position: absolute; top: 947px; left: 0; right: 0;
    text-align: center;
    font: 600 32px/33px "Dancing Script", cursive;
    color: var(--paper);
  }
  .site-bar {
    position: absolute; bottom: 0; left: 0; right: 0; height: 33px;
    background: var(--deep-green);
    color: var(--paper);
    font: 700 11.5px/33px "Montserrat", sans-serif;
    text-align: center;
    letter-spacing: 0.2px;
  }
</style>
</head>
<body>

<svg width="0" height="0" style="position:absolute">
  <defs>
    <linearGradient id="green-rise" x1="0" y1="0" x2="0" y2="1">
      <stop offset="0" stop-color="#00934a" stop-opacity="0"/>
      <stop offset="0.45" stop-color="#00934a" stop-opacity="0.85"/>
      <stop offset="0.6" stop-color="#00934a"/>
      <stop offset="1" stop-color="#00934a"/>
    </linearGradient>
  </defs>
</svg>

<section class="strip strip--one">
  <div class="brand-name">Tavrenwick Lending</div>
  <div class="offer-intro">We Offer</div>
  <div class="loan-type">Unsecured Loans<br>Up To</div>
  <div class="loan-amount">$40,000</div>
  <div class="photo-area" role="img" aria-label="Photo of two smiling men in smart clothes looking at a tablet together"></div>
  <svg class="pin-graphic" viewBox="0 0 241 1087" aria-hidden="true">
    <rect x="0" y="700" width="241" height="360" fill="url(#green-rise)"/>
    <path d="M120.5 668 A122 122 0 0 1 211 872 L120.5 940 L30 872 A122 122 0 0 1 120.5 668 Z" fill="#ffffff" opacity="0.3"/>
    <path d="M120.5 692 A98 98 0 0 1 190 858 L120.5 908 L51 858 A98 98 0 0 1 120.5 692 Z" fill="#ffffff" opacity="0.55"/>
    <circle cx="120.5" cy="790" r="74" fill="#00934a"/>
  </svg>
  <div class="apply-note">Customer<br>Can Apply<br>Online Or Over<br>The Phone</div>
  <div class="speed-line">that the process<br>is quick</div>
  <div class="site-bar">www.tavrenwick lending.example</div>
</section>

<section class="strip strip--two">
  <div class="brand-name">Tavrenwick Lending</div>
  <div class="offer-intro">We Offer</div>
  <div class="loan-type">Unsecured Loans<br>Up To</div>
  <div class="loan-amount">$40,000</div>
  <div class="photo-area" role="img" aria-label="Photo of two smiling men in smart clothes looking at a tablet together"></div>
  <svg class="pin-graphic" viewBox="0 0 241 1087" aria-hidden="true">
    <rect x="0" y="700" width="241" height="360" fill="url(#green-rise)"/>
    <path d="M120.5 668 A122 122 0 0 1 211 872 L120.5 940 L30 872 A122 122 0 0 1 120.5 668 Z" fill="#ffffff" opacity="0.3"/>
    <path d="M120.5 692 A98 98 0 0 1 190 858 L120.5 908 L51 858 A98 98 0 0 1 120.5 692 Z" fill="#ffffff" opacity="0.55"/>
    <circle cx="120.5" cy="790" r="74" fill="#00934a"/>
  </svg>
  <div class="apply-note">Customer<br>Can Apply<br>Online Or Over<br>The Phone</div>
  <div class="speed-line">that the process<br>is quick</div>
  <div class="site-bar">www.tavrenwick lending.example</div>
</section>

<section class="strip strip--three">
  <div class="brand-name">Tavrenwick Lending</div>
  <div class="offer-intro">We Offer</div>
  <div class="loan-type">Unsecured Loans<br>Up To</div>
  <div class="loan-amount">$40,000</div>
  <div class="photo-area" role="img" aria-label="Photo of two smiling men in smart clothes looking at a tablet together"></div>
  <svg class="pin-graphic" viewBox="0 0 241 1087" aria-hidden="true">
    <rect x="0" y="700" width="241" height="360" fill="url(#green-rise)"/>
    <path d="M120.5 668 A122 122 0 0 1 211 872 L120.5 940 L30 872 A122 122 0 0 1 120.5 668 Z" fill="#ffffff" opacity="0.3"/>
    <path d="M120.5 692 A98 98 0 0 1 190 858 L120.5 908 L51 858 A98 98 0 0 1 120.5 692 Z" fill="#ffffff" opacity="0.55"/>
    <circle cx="120.5" cy="790" r="74" fill="#00934a"/>
  </svg>
  <div class="apply-note">Customer<br>Can Apply<br>Online Or Over<br>The Phone</div>
  <div class="speed-line">that the process<br>is quick</div>
  <div class="site-bar">www.tavrenwick lending.example</div>
</section>

</body>
</html>
```